Need Bold, Hip Card for Concert Ticket Website Gleaming Passes!

Hi there! I am putting together a business/website that sells event tickets (mostly concerts, but also some sports and theater). Think SeatNook, but much smaller. The site is called Gleaming Passes. I have a new logo (attached, with black/red/white color scheme), and am looking for a modern/cool/original business card design. Note that I am thinking of having the card itself in the shape of a ticket (die cut), so you may want to keep that in mind when designing, but I'm not set on that. I'm also open to alternative card sizes, thicknesses, glossy, spot UV, etc. in order to stand out. I'm attaching a potential die cut template and a sample card using that template in case you want to work with that.
Target Market(s)
Music fans, people that like going to see live events
Industry/Entity Type
Entertainment
Contact Information for Business Card
Information that I'd like to have:
website address - www.gleamingpasses.example
phone number: 1-833-5GLEAMNG (532-6264)
my name - Wendel Pike

```html
<!DOCTYPE html>
<html lang="en">
<head>
<meta charset="utf-8">
<title>Gleaming Passes – Business Card</title>
<link href="https://fonts.googleapis.com/css2?family=Montserrat:wght@800&family=Open+Sans:wght@400;700&family=Oswald:wght@500&display=swap" rel="stylesheet">
<style>
  :root {
    --backdrop: #161717;
    --card-dark: #262626;
    --card-light: #ecedf0;
    --brand-red: #a3171c;
    --ink-dark: #2a2a2a;
    --ink-grey: #5d5d62;
    --mark-faint: #d9d2d5;
  }
  * { margin: 0; padding: 0; box-sizing: border-box; }
  html, body {
    width: 1200px; height: 750px; overflow: hidden;
    background: var(--backdrop);
  }
  .stage {
    width: 1200px; height: 750px;
    display: flex; flex-direction: column;
    align-items: center; justify-content: center; gap: 62px;
  }
  .card {
    width: 472px; height: 260px; position: relative;
    box-shadow: 0 18px 30px rgba(0,0,0,.55);
  }
  .card--front { background: var(--card-dark); }
  .card--back { background: var(--card-light); }

  .wordmark {
    display: flex; align-items: center; gap: 10px;
    font-family: "Montserrat", sans-serif; font-weight: 800;
    text-transform: uppercase; color: var(--brand-red);
    letter-spacing: .02em; line-height: 1;
  }
  .wordmark__square { width: 26px; height: 26px; background: var(--brand-red); flex: none; }

  .card--front .wordmark {
    position: absolute; left: 50%; top: 50%;
    transform: translate(-50%, -50%); font-size: 30px; white-space: nowrap;
  }

  .card--back .wordmark {
    position: absolute; left: 50%; top: 12px;
    transform: translateX(-50%); font-size: 26px; white-space: nowrap;
  }
  .faint-mark {
    position: absolute; left: 50%; top: 86px; transform: translateX(-50%);
    width: 70px; height: 100px; background: var(--mark-faint); opacity: .7;
  }

  .contact {
    position: absolute; left: 0; right: 0; bottom: 14px;
    display: flex; justify-content: center; align-items: stretch;
  }
  .contact__person { text-align: right; padding-right: 11px; }
  .contact__name {
    font-family: "Open Sans", sans-serif; font-weight: 400;
    font-size: 23px; line-height: 1; color: var(--ink-grey); letter-spacing: -.01em;
  }
  .contact__role {
    font-family: "Open Sans", sans-serif; font-weight: 700;
    font-size: 16px; line-height: 1.2; color: var(--ink-dark);
  }
  .contact__divider { width: 1.5px; background: var(--ink-dark); }
  .contact__details {
    padding-left: 11px; display: flex; flex-direction: column; justify-content: center; gap: 3px;
    font-family: "Oswald", sans-serif; font-weight: 500; font-size: 10.5px; color: var(--ink-dark);
  }
  .contact__line { display: flex; align-items: center; gap: 9px; }
  .contact__line svg { width: 9px; height: 9px; flex: none; }
</style>
</head>
<body>
<main class="stage">
  <section class="card card--front" aria-label="Card front">
    <div class="wordmark"><span class="wordmark__square"></span>Gleaming Passes</div>
  </section>

  <section class="card card--back" aria-label="Card back">
    <div class="wordmark">Gleaming Passes</div>
    <div class="faint-mark" role="img" aria-label="Faint brand mark decoration"></div>
    <div class="contact">
      <div class="contact__person">
        <p class="contact__name">Wendel Pike</p>
        <p class="contact__role">Director</p>
      </div>
      <div class="contact__divider"></div>
      <div class="contact__details">
        <p class="contact__line">
          <svg viewBox="0 0 24 24" aria-hidden="true"><path fill="#2a2a2a" d="M6.6 10.8a15 15 0 0 0 6.6 6.6l2.2-2.2c.3-.3.7-.4 1-.2 1.1.4 2.3.6 3.6.6.6 0 1 .4 1 1V20c0 .6-.4 1-1 1A17 17 0 0 1 3 4c0-.6.4-1 1-1h3.5c.6 0 1 .4 1 1 0 1.3.2 2.5.6 3.6.1.3 0 .7-.2 1z"/></svg>
          1-833-5GLEAMNG
        </p>
        <p class="contact__line">
          <svg viewBox="0 0 24 24" aria-hidden="true"><g fill="none" stroke="#2a2a2a" stroke-width="2.4"><circle cx="12" cy="12" r="9.5"/><ellipse cx="12" cy="12" rx="4" ry="9.5"/><path d="M2.5 12h19"/></g></svg>
          www.gleamingpasses.example
        </p>
      </div>
    </div>
  </section>
</main>
</body>
</html>
```